create a template CSS for all pages of my website

I need a template CSS that can be easily modified, that can be used on all pages of my website. I have included all the image files (Header & footer) to be displayed on each page. You can choose to use #1 or #2 headers and footers. You may also decided to provide your entry in two separate entries using #1 and then using #2 (The only difference between the two is the color of the font). I have also included JPG & PNG files, depending on which you like to work with best ( I would prefer you use the png).

What I am looking for, is a back ground & color scheme to go with my header & footer. You may add any types of HTML5 components to your html file when displaying your entry, but the CSS should be a separate file from the HTML file with the header & footer (i.e., no embedded CSS).

What I am looking for

1.) Originality
2.) Background color and image to go with CSS
3.) color scheme that flows well with header and footer and helps convey the message

Please be sure to take screenshots of your work loaded in a webbrowser.

NOTE: I am one to not wait until the contest ends. If I see one that I really like , I will award right away. I also give lots of feedback, so don't wait until the last minute to submit, because you may lose out. Submit your early work and let me help you mold it into the winner <smile>

```html
<!DOCTYPE html>
<html lang="en">
<head>
<meta charset="utf-8">
<title>Pinewood Trail List</title>
<link href="https://fonts.googleapis.com/css2?family=Arimo:wght@400;700&display=swap" rel="stylesheet">
<style>
:root{
  --nav-top:#4f93c9;
  --nav-bottom:#2f6fae;
  --nav-active:#f5e61a;
  --grass:#85a85a;
  --grass-mid:#a9ba7e;
  --sand:#e6e0c6;
  --panel:#e8e3cf;
  --panel-border:#b89d5c;
  --ink:#2f2a20;
  --body-ink:#2e2e22;
  --link:#f2e23a;
  --accent:#2b8fd6;
  --btn:#0d5fc2;
  --rule:#f4f1e4;
}
*{box-sizing:border-box;margin:0;padding:0}
html,body{width:979px;height:1200px;overflow:hidden}
body{
  position:relative;
  font-family:"Arimo",Arial,sans-serif;
  color:var(--body-ink);
  background:linear-gradient(180deg,var(--grass) 0,var(--grass) 300px,var(--grass-mid) 600px,#d3d0a9 850px,var(--sand) 1000px,var(--sand) 1200px);
}
.navbar{position:absolute;top:0;left:0;width:979px;height:22px;background:linear-gradient(var(--nav-top),var(--nav-bottom));}
.navbar .brand{position:absolute;left:188px;top:4px;font-size:11px;color:#e6eef6}
.nav-links{position:absolute;left:258px;top:0;display:flex;list-style:none;font-size:8px}
.nav-links li{padding:6px 8px;color:#dce8f3;height:22px}
.nav-links li.active{background:var(--nav-active);color:#333}
.signin{position:absolute;left:576px;top:2px;display:flex;gap:4px}
.signin .field{width:88px;height:16px;background:#fff;border:1px solid #9bb;font-size:7px;color:#999;padding:3px 4px}
.signin .btn-sign{width:36px;height:16px;background:#f1f1f1;border:1px solid #aaa;border-radius:3px;font-size:8px;text-align:center;line-height:14px;color:#333}
.header-scene{position:absolute;top:22px;left:0;width:979px;height:52px;background:linear-gradient(180deg,#ece6cd 0,#e1d9b6 60%,#8fae62 100%)}
.brandmark{position:absolute;display:flex;align-items:center;gap:6px;font-weight:700;color:#3f8ec9;text-transform:uppercase}
.brandmark .dot{border-radius:50%;background:#d9a53a}
.brandmark.top{left:396px;top:40px;font-size:12px}
.brandmark.top .dot{width:22px;height:22px}
.hero{position:absolute;left:190px;top:89px;width:601px;height:167px;background:var(--panel);border:4px solid var(--panel-border);border-radius:34px;box-shadow:0 0 0 2px #ede3c2 inset,0 2px 4px rgba(0,0,0,.25);padding:34px 32px}
.hero h1{font-size:31px;color:var(--ink);letter-spacing:-.5px;line-height:1}
.hero p{font-size:9.5px;line-height:15px;margin:10px 0 10px;color:#222;width:510px}
.btn-primary{display:inline-block;background:linear-gradient(#2a7fe0,var(--btn));color:#fff;font-size:9px;padding:6px 11px;border-radius:4px}
.cols{position:absolute;left:188px;top:277px;width:603px;display:flex;justify-content:space-between}
.col{width:190px}
h2,h3{color:#fff;text-shadow:1px 1px 2px rgba(0,0,0,.45);font-weight:700}
.col h2{font-size:17.5px;margin-bottom:6px}
.small{font-size:7.6px;line-height:10.3px}
.btn-default{display:inline-block;margin-top:6px;background:#fafafa;border:1px solid #bbb;border-radius:3px;font-size:7.6px;padding:3px 7px;color:#333}
.rule{position:absolute;left:188px;top:388px;width:603px;height:2px;background:var(--rule)}
.featurette{position:absolute;left:188px;top:401px;width:603px}
.featurette h2{font-size:17px}
.featurette h2 span{color:var(--accent)}
.featurette p{font-size:11.2px;line-height:16px;margin-top:6px;color:#222}
.main{position:absolute;left:188px;top:474px;width:392px}
.main h2{font-size:17px;margin-bottom:6px}
.main h3{font-size:12.5px;margin:10px 0 5px}
.main p{margin-bottom:6px}
a.hl{color:var(--link)}
ul,ol{padding-left:13px}
dl dt{font-weight:700}
dl dd{padding-left:6px}
blockquote{border-left:3px solid #eee9d3;padding-left:10px;font-size:10.2px;line-height:12.5px;margin-top:6px;color:#222}
table{border-collapse:collapse;font-size:7.6px;margin-top:6px}
th{text-align:left;padding:6px 4px 6px 4px}
td{padding:6px 4px 6px 4px}
.side{position:absolute;left:600px;top:474px;width:191px}
.side h2{font-size:13.5px;margin-bottom:8px}
.side ul,.side ol{margin-bottom:6px}
.footer-scene{position:absolute;left:0;top:1040px;width:979px;height:160px;background:linear-gradient(180deg,rgba(230,224,198,0) 0,#ddd5b3 40%,#d9cfa6 65%,#8fae62 82%,#7c9d55 100%)}
.brandmark.bottom{left:264px;top:1094px;font-size:11px}
.brandmark.bottom .dot{width:20px;height:20px}
</style>
</head>
<body>
<nav class="navbar">
  <span class="brand">Project name</span>
  <ul class="nav-links">
    <li class="active">Home</li><li>About</li><li>Contact</li><li>Dropdown ▾</li>
  </ul>
  <div class="signin">
    <span class="field">Email</span><span class="field">Password</span><span class="btn-sign">Sign in</span>
  </div>
</nav>

<div class="header-scene" role="img" aria-label="Mountain landscape banner with pine trees and a deer"></div>
<div class="brandmark top"><span class="dot"></span>Pinewood Trail List</div>

<section class="hero">
  <h1>Hello, world!</h1>
  <p>This is a template for a simple marketing or informational website. It includes a large callout called the hero unit and three supporting pieces of content. Use it as a starting point to create something more unique.</p>
  <span class="btn-primary">Learn more »</span>
</section>

<section class="cols">
  <div class="col"><h2>Heading</h2><p class="small">Donec id elit non mi porta gravida at eget metus. Fusce dapibus, tellus ac cursus commodo, tortor mauris condimentum nibh, ut fermentum massa justo sit amet risus. Etiam porta sem malesuada magna mollis euismod. Donec sed odio dui.</p><span class="btn-default">View details »</span></div>
  <div class="col"><h2>Heading</h2><p class="small">Donec id elit non mi porta gravida at eget metus. Fusce dapibus, tellus ac cursus commodo, tortor mauris condimentum nibh, ut fermentum massa justo sit amet risus. Etiam porta sem malesuada magna mollis euismod. Donec sed odio dui.</p><span class="btn-default">View details »</span></div>
  <div class="col"><h2>Heading</h2><p class="small">Donec sed odio dui. Cras justo odio, dapibus ac facilisis in, egestas eget quam. Vestibulum id ligula porta felis euismod semper. Fusce dapibus, tellus ac cursus commodo, tortor mauris condimentum nibh, ut fermentum massa justo sit amet risus.</p><span class="btn-default">View details »</span></div>
</section>

<div class="rule"></div>

<section class="featurette">
  <h2>First featurette headling. <span>It'll blow your mind.</span></h2>
  <p>Donec ullamcorper nulla non metus auctor fringilla. Vestibulum id ligula porta felis euismod semper. Praesent commodo cursus magna, vel scelerisque nisl consectetur. Fusce dapibus, tellus ac cursus commodo.</p>
</section>

<main class="main small">
  <h2>Paragraphs</h2>
  <p>Lorem ipsum dolor sit amet, <a class="hl">consectetur adipisicing</a> elit, sed do eiusmod tempor incididunt ut labore et dolore magna aliqua. Ut enim ad minim veniam, quis nostrud exercitation ullamco laboris nisi ut aliquip ex ea commodo consequat. Duis aute irure dolor in reprehenderit in voluptate velit esse cillum dolore eu fugiat nulla pariatur. Excepteur sint occaecat cupidatat non proident, sunt in culpa qui officia deserunt mollit anim id est laborum.</p>
  <p><b>Lorem ipsum dolor sit amet, consectetur adipisicing elit,</b> sed do eiusmod tempor incididunt ut labore et dolore magna aliqua. Ut enim ad minim veniam, quis <a class="hl">nostrud exercitation</a> ullamco laboris nisi ut aliquip ex ea commodo consequat. Duis aute irure dolor in reprehenderit in voluptate velit esse cillum dolore eu fugiat nulla pariatur. Excepteur sint occaecat cupidatat non proident, sunt in culpa qui officia deserunt mollit anim id est laborum.</p>
  <h3>Unordered lists</h3>
  <ul><li>Lorem ipsum dolor sit amet</li><li>Consectetur adipisicing elit</li><li>Sed do eiusmod tempor incididunt ut labore et dolore magna aliqua</li><li>Ut enim ad minim veniam</li></ul>
  <h3>Ordered lists</h3>
  <ol><li>Consectetur adipisicing elit</li><li>Sed do eiusmod tempor incididunt ut labore</li><li>Et dolore magna aliqua</li></ol>
  <h3>Definition lists</h3>
  <dl>
    <dt>Lorem ipsum dolor sit amet</dt><dd>Consectetur adipisicing elit, sed do eiusmod tempor incididunt ut labore et dolore magna aliqua.</dd>
    <dt>Ut enim ad minim veniam</dt><dd>Quis nostrud exercitation ullamco laboris nisi ut aliquip ex ea commodo consequat.</dd>
    <dt>Duis aute irure dolor</dt><dd>In reprehenderit in voluptate velit esse cillum dolore eu fugiat nulla pariatur.</dd>
    <dt>Excepteur sint occaecat</dt><dd>Cupidatat non proident, sunt in culpa qui officia deserunt mollit anim id est laborum.</dd>
  </dl>
  <h3>Blockquotes</h3>
  <blockquote>Lorem ipsum dolor sit amet, consectetur adipisicing elit, sed do eiusmod tempor incididunt ut labore et dolore magna aliqua. Ut enim ad minim veniam, quis nostrud exercitation ullamco laboris nisi ut aliquip ex ea commodo consequat. Duis aute irure dolor in reprehenderit in voluptate velit esse cillum dolore eu fugiat nulla pariatur. Excepteur sint occaecat cupidatat non proident, sunt in culpa qui officia deserunt mollit anim id est laborum.</blockquote>
  <h3>Tables</h3>
  <table>
    <thead><tr><th>Item</th><th>Quantity</th><th>Price</th></tr></thead>
    <tbody><tr><td>Lorem ipsum dolor</td><td>1</td><td>$10.00</td></tr><tr><td>Adipisicing elit</td><td>2</td><td>$12.00</td></tr></tbody>
  </table>
</main>

<aside class="side small">
  <h2>Commodo consequat</h2>
  <ul>
    <li><a class="hl">Consectetur adipisicing elit</a> sed do eiusmod tempor incididunt ut labore</li>
    <li><a class="hl">Quis nostrud exercitation</a> ullamco laboris nisi ut aliquip</li>
  </ul>
  <ul><li>Lorem ipsum dolor sit amet</li><li>Consectetur adipisicing elit</li><li>Sed do eiusmod tempor incididunt ut labore et dolore magna aliqua</li><li>Ut enim ad minim veniam</li></ul>
  <ol><li>Consectetur adipisicing elit</li><li>Sed do eiusmod tempor incididunt ut labore</li><li>Et dolore magna aliqua</li></ol>
</aside>

<footer class="footer-scene" role="img" aria-label="Landscape footer with clouds, hills, a hiker on a trail, pine trees and a lake"></footer>
<div class="brandmark bottom"><span class="dot"></span>Pinewood Trail List</div>
</body>
</html>
```